Ridgeline Wild Craft DL flyer

I'm looking for a new flyer for my startup business. In Darwin Australia.
Aimed at family's and short stay tourists the "Ridgeline Wild Craft" 4 hr tour will give people a basic understanding of some essential bush survival skills in the Australian Outback.
things covered in this 4 hr tour are
1. Finding water.
2. finding food.
3. Finding/making shelter and fire.
4. Finding your way home.

The tour will pick clients up in an air conditioned purpose build 4WD and take them to a nearby bushland area where they will have the opportunity to catch and harvest some native bushtucker.
They will then be able to find/harvest some water for survival situations.
While we cook our bush tucker they will also learn to find their way home through ancient navigation techniques as well.

Clients will then be dropped back to their accomodation with some fun and vital knowledge of surviving in the Australian outback.
At the end of the tour the group will be able to take home a basic survival kit which they will be able to use through the skills they just gained on the tour.

I'd like a two sided DL size flyer emphasising the following points.
4hr/half day tour
Fun for the family
Free survival kit included.
Eat what you catch
Learn essential survival skills
Provided buy an experienced and passionate bushman.
$150/head including transfers.

I'll provide some pictures for the flyer and any extra content you require.

Target Market(s)

Family's
Short stay tourists

Industry/Entity Type

Tourism

Colors

Designer to choose colors to be used in the design.

Requirements
Must have
• As per brief
Nice to have
• Any extra content and flair designers would like to add
Should not have
• Any images which aren't Australian

```html
<!DOCTYPE html>
<html lang="en">
<head>
<meta charset="utf-8">
<title>Ridgeline Wild Craft – DL Flyer</title>
<link href="https://fonts.googleapis.com/css2?family=Montserrat:wght@500;700&family=Lato:wght@400;700&family=Oswald:wght@600;700&family=Russo+One&display=swap" rel="stylesheet">
<style>
  :root{
    --sky:#3db4e5;
    --sky-deep:#1f8fc4;
    --ink:#111214;
    --charcoal:#2a2b2e;
    --paper:#f4f4f4;
    --mist:#d2d3d5;
    --stage:#e4e4e4;
    --white:#ffffff;
  }
  *{margin:0;padding:0;box-sizing:border-box}
  html,body{width:1200px;height:1200px;overflow:hidden;background:var(--stage)}
  .stage{position:relative;width:1200px;height:1200px}
  .flyer{position:absolute;top:60px;width:540px;height:1080px;overflow:hidden;
    background:linear-gradient(180deg,var(--paper) 0%,#dedfe1 45%,var(--paper) 70%,#e2e3e5 100%);
    font-family:'Lato',sans-serif;color:var(--ink)}
  .flyer--front{left:40px}
  .flyer--back{left:620px}
  .flyer__art{position:absolute;inset:0;width:540px;height:1080px}
  .flyer__text{position:absolute}

  .brand{left:0;width:540px;top:18px;text-align:center}
  .brand__name{font-family:'Montserrat',sans-serif;font-weight:700;font-size:48px;color:var(--sky);letter-spacing:1px;line-height:1}
  .brand__tag{font-family:'Montserrat',sans-serif;font-weight:500;font-size:27px;color:var(--white);letter-spacing:10px;margin-top:12px;line-height:1}

  .price{left:293px;width:230px;top:488px;text-align:center}
  .price__amount{font-family:'Oswald',sans-serif;font-weight:700;font-size:64px;color:var(--sky);line-height:1}
  .price__note{font-family:'Montserrat',sans-serif;font-weight:700;font-size:12px;color:var(--sky);margin-top:6px}
  .price__main{font-family:'Montserrat',sans-serif;font-weight:500;font-size:18px;color:var(--white);margin-top:3px}

  .intro{left:35px;width:480px;top:702px;font-size:17.5px;line-height:1.25}
  .topics-title{left:38px;top:791px;font-size:16px;color:var(--white)}
  .topics{left:34px;top:842px;width:320px;font-size:14.5px;line-height:1.2}
  .topic{position:absolute;display:flex;gap:8px;align-items:flex-start;white-space:nowrap}
  .topic svg{flex:none;width:24px;height:24px}

  .call{font-family:'Russo One',sans-serif;color:var(--white);white-space:nowrap;letter-spacing:1px}
  .call--front{left:42px;top:950px;font-size:18px;transform:rotate(15.5deg);transform-origin:left top}

  .story{left:34px;width:480px;font-size:14.5px;line-height:1.3;font-weight:700}
  .story p+p{margin-top:18px}

  .feature{position:absolute;width:170px;margin-left:-85px;text-align:center;font-size:15px;font-weight:700;line-height:1.25}
  .call--back{left:262px;top:1021px;font-family:'Montserrat',sans-serif;font-weight:700;font-size:17px;transform:rotate(-16.4deg);transform-origin:left top}
  .web{left:254px;top:1047px;font-family:'Montserrat',sans-serif;font-weight:700;font-size:14px;letter-spacing:3px;color:var(--white)}
</style>
</head>
<body>
<div class="stage">

  <section class="flyer flyer--front">
    <svg class="flyer__art" viewBox="0 0 540 1080">
      <defs>
        <linearGradient id="bushScene" x1="0" y1="0" x2="0" y2="1">
          <stop offset="0" stop-color="#e9ece8"/>
          <stop offset="0.35" stop-color="#7f9a62"/>
          <stop offset="0.7" stop-color="#6f7f3e"/>
          <stop offset="1" stop-color="#9a5a30"/>
        </linearGradient>
        <linearGradient id="guidePhoto" x1="0" y1="0" x2="1" y2="1">
          <stop offset="0" stop-color="#b9b1a0"/>
          <stop offset="0.5" stop-color="#a3775a"/>
          <stop offset="1" stop-color="#d9dad3"/>
        </linearGradient>
      </defs>
      <polygon points="0,0 540,0 540,22 290,262 250,262 0,22" fill="var(--ink)"/>
      <polygon points="300,40 540,10 540,30 330,230" fill="#2c2d31"/>
      <line x1="0" y1="24" x2="232" y2="246" stroke="var(--sky)" stroke-width="7"/>
      <line x1="540" y1="24" x2="308" y2="246" stroke="var(--sky)" stroke-width="7"/>
      <polygon points="540,118 540,142 405,277 380,277" fill="var(--ink)"/>
      <polygon points="540,150 540,160 420,280 410,280" fill="var(--sky)"/>
      <polygon points="0,620 120,520 140,530 0,650" fill="var(--ink)"/>
      <polygon points="0,660 150,535 160,542 0,672" fill="var(--sky)"/>
      <polygon points="260,124 533,397 260,670 -13,397" fill="var(--sky)"/>
      <polygon points="260,136 521,397 260,658 -1,397" fill="var(--white)"/>
      <g role="img" aria-label="Photo of outback bushland with tall termite mounds among green grass and gum trees">
        <polygon points="260,144 513,397 260,650 7,397" fill="url(#bushScene)"/>
      </g>
      <polygon points="408,393 561,546 408,699 255,546" fill="var(--sky)"/>
      <polygon points="408,405 549,546 408,687 267,546" fill="var(--white)"/>
      <polygon points="408,413 541,546 408,679 275,546" fill="var(--ink)"/>
      <circle cx="408" cy="464" r="8" fill="#9a9b9e" stroke="var(--white)" stroke-width="2"/>
      <path d="M0,782 H320 a18,18 0 0 1 0,36 H0 Z" fill="var(--ink)"/>
      <path d="M0,778 H322 a22,22 0 0 1 0,44 H0" fill="none" stroke="var(--sky)" stroke-width="2"/>
      <g role="img" aria-label="Photo of the bushman guide in a wide-brim hat and sunglasses">
        <polygon points="372,800 540,780 540,1080 300,1080 340,900" fill="url(#guidePhoto)"/>
      </g>
      <polygon points="0,929 320,1018 320,1060 0,971" fill="var(--ink)"/>
      <polygon points="0,971 320,1060 360,1080 0,1080" fill="var(--sky)"/>
      <polygon points="0,1020 200,1080 0,1080" fill="var(--sky-deep)" opacity="0.5"/>
    </svg>

    <div class="flyer__text brand">
      <div class="brand__name">RIDGELINE</div>
      <div class="brand__tag">WILD CRAFT</div>
    </div>

    <div class="flyer__text price">
      <div class="price__amount">$150</div>
      <div class="price__note">HEAD INCLUDING</div>
      <div class="price__main">TRANSFERS</div>
    </div>

    <p class="flyer__text intro">4 hrs tour will give people a basic understanding of some essential bush survival skills in the Australian Outback.</p>

    <p class="flyer__text topics-title">Things covered in this 4 hrs tour are</p>

    <div class="flyer__text topics">
      <div class="topic" style="left:0;top:0">
        <svg viewBox="0 0 26 26"><circle cx="13" cy="13" r="11" fill="var(--sky)" stroke="var(--sky-deep)" stroke-width="2"/><path d="M13 6 C10 11 9 13 9 15 a4 4 0 0 0 8 0 C17 13 16 11 13 6Z" fill="var(--white)"/></svg>
        <span>Finding water</span>
      </div>
      <div class="topic" style="left:0;top:32px">
        <svg viewBox="0 0 26 26"><circle cx="13" cy="13" r="11" fill="var(--sky)" stroke="var(--sky-deep)" stroke-width="2"/><path d="M7 12 H19 a6 6 0 0 1 -12 0Z" fill="var(--white)"/></svg>
        <span>finding food</span>
      </div>
      <div class="topic" style="left:155px;top:0">
        <svg viewBox="0 0 26 26"><circle cx="13" cy="13" r="11" fill="var(--sky)" stroke="var(--sky-deep)" stroke-width="2"/><path d="M13 5 C15 9 18 11 18 15 a5 5 0 0 1 -10 0 C8 12 10 11 11 8 C12 10 13 10 13 5Z" fill="var(--white)"/></svg>
        <span>Finding/making<br>shelter and fire.</span>
      </div>
      <div class="topic" style="left:155px;top:44px">
        <svg viewBox="0 0 26 26"><circle cx="13" cy="13" r="11" fill="var(--sky)" stroke="var(--sky-deep)" stroke-width="2"/><circle cx="13" cy="13" r="6" fill="none" stroke="var(--white)" stroke-width="1.8"/><path d="M13 8 L15 13 L13 18 L11 13Z" fill="var(--white)"/></svg>
        <span>Finding your way<br>home.</span>
      </div>
    </div>

    <div class="flyer__text call call--front">CALL US-00 0000 000</div>
  </section>

  <section class="flyer flyer--back">
    <svg class="flyer__art" viewBox="0 0 540 1080">
      <defs>
        <linearGradient id="fruitPhoto" x1="0" y1="0" x2="1" y2="1">
          <stop offset="0" stop-color="#c9a58a"/><stop offset="0.5" stop-color="#6f9a3a"/><stop offset="1" stop-color="#8a7a55"/>
        </linearGradient>
        <linearGradient id="branchPhoto" x1="0" y1="0" x2="1" y2="1">
          <stop offset="0" stop-color="#a8c4d8"/><stop offset="0.5" stop-color="#6b5a40"/><stop offset="1" stop-color="#e09a2a"/>
        </linearGradient>
        <linearGradient id="palmPhoto" x1="0" y1="0" x2="0" y2="1">
          <stop offset="0" stop-color="#eef0ea"/><stop offset="0.4" stop-color="#7ea13e"/><stop offset="1" stop-color="#3f5a24"/>
        </linearGradient>
        <linearGradient id="crabPhoto" x1="0" y1="0" x2="1" y2="1">
          <stop offset="0" stop-color="#c89a78"/><stop offset="0.6" stop-color="#8a6a50"/><stop offset="1" stop-color="#4a5a4a"/>
        </linearGradient>
      </defs>
      <polygon points="0,0 40,0 0,40" fill="var(--sky)"/>
      <polygon points="0,0 80,0 150,70 130,90" fill="var(--ink)"/>
      <polygon points="0,140 0,330 120,210" fill="var(--sky)"/>
      <polygon points="0,330 0,370 230,140 230,100" fill="var(--ink)"/>
      <polygon points="0,370 0,380 240,140 240,130" fill="var(--sky)"/>
      <polygon points="540,200 540,420 430,310" fill="var(--sky)"/>
      <polygon points="540,390 540,470 390,320 430,310" fill="var(--ink)"/>
      <polygon points="540,470 540,480 380,320 390,320" fill="var(--sky)"/>

      <polygon points="145,8 277,140 145,272 13,140" fill="var(--sky)"/>
      <polygon points="145,18 267,140 145,262 23,140" fill="var(--white)"/>
      <g role="img" aria-label="Photo of a hand holding green native bush fruit"><polygon points="145,26 259,140 145,254 31,140" fill="url(#fruitPhoto)"/></g>

      <polygon points="423,8 555,140 423,272 291,140" fill="var(--sky)"/>
      <polygon points="423,18 545,140 423,262 301,140" fill="var(--white)"/>
      <g role="img" aria-label="Photo of a bush branch with ripening orange fruit"><polygon points="423,26 537,140 423,254 309,140" fill="url(#branchPhoto)"/></g>

      <polygon points="286,150 460,324 286,498 112,324" fill="var(--sky)"/>
      <polygon points="286,160 450,324 286,488 122,324" fill="var(--white)"/>
      <g role="img" aria-label="Photo of a pandanus palm with spiky green fronds"><polygon points="286,168 442,324 286,480 130,324" fill="url(#palmPhoto)"/></g>

      <line x1="60" y1="627" x2="480" y2="627" stroke="#c4c5c7" stroke-width="3"/>

      <line x1="89" y1="687" x2="444" y2="687" stroke="var(--sky)" stroke-width="5"/>
      <line x1="89" y1="823" x2="444" y2="823" stroke="var(--sky)" stroke-width="5"/>

      <g class="feature-icons" fill="var(--ink)">
        <g stroke="var(--sky)" stroke-width="3" fill="var(--white)">
          <polygon points="89,652 124,687 89,722 54,687"/>
          <polygon points="270,652 305,687 270,722 235,687"/>
          <polygon points="444,652 479,687 444,722 409,687"/>
          <polygon points="89,788 124,823 89,858 54,823"/>
          <polygon points="270,788 305,823 270,858 235,823"/>
          <polygon points="444,788 479,823 444,858 409,823"/>
        </g>
        <circle cx="92" cy="674" r="3"/>
        <path d="M91 678 L87 690 L82 700 M89 686 L95 700 M90 681 L97 686" stroke="var(--ink)" stroke-width="3" fill="none" stroke-linecap="round"/>
        <rect x="81" y="679" width="5" height="9" rx="1"/>
        <circle cx="262" cy="675" r="3"/><circle cx="278" cy="675" r="3"/><circle cx="270" cy="683" r="2.4"/>
        <rect x="259" y="679" width="6" height="19" rx="2"/><rect x="275" y="679" width="6" height="19" rx="2"/><rect x="268" y="686" width="4" height="11" rx="1.5"/>
        <rect x="432" y="678" width="24" height="19" rx="2"/>
        <rect x="439" y="674" width="10" height="5" fill="none" stroke="var(--ink)" stroke-width="2"/>
        <path d="M444 682 V693 M438.5 687.5 H449.5" stroke="var(--white)" stroke-width="2.5"/>
        <path d="M80 814 a10 10 0 1 1 12 16 L84 830" fill="none" stroke="var(--ink)" stroke-width="4" stroke-linecap="round"/>
        <circle cx="95" cy="812" r="3"/>
        <path d="M259 838 L270 812 L281 838 M270 812 L264 806 M270 812 L276 806" fill="none" stroke="var(--ink)" stroke-width="3" stroke-linecap="round"/>
        <path d="M266 838 L270 830 L274 838Z"/>
        <circle cx="450" cy="809" r="3"/>
        <path d="M448 813 L442 825 L434 832 M442 825 L450 830 L452 838 M446 817 L454 820 M446 817 L438 818" fill="none" stroke="var(--ink)" stroke-width="2.6" stroke-linecap="round"/>
      </g>

      <polygon points="160,1080 540,968 540,1080" fill="var(--ink)"/>
      <polygon points="170,1035 540,926 540,968 180,1074" fill="var(--sky)"/>
      <g role="img" aria-label="Photo of the bushman holding up a freshly caught mud crab">
        <polygon points="0,975 60,910 150,918 240,1000 250,1080 0,1080" fill="url(#crabPhoto)"/>
      </g>
    </svg>

    <div class="flyer__text story" style="top:493px">
      <p>Clients will then be dropped back to their accomodation with some fun and vital knowledge of surviving in the Australian outback.</p>
      <p>At the end of the tour the group will be able to take home a basic survival kit which they will be able to use through the skills they just gained on the tour.</p>
    </div>

    <div class="feature" style="left:94px;top:742px">4hr/half day tour</div>
    <div class="feature" style="left:276px;top:745px">Fun for the family</div>
    <div class="feature" style="left:438px;top:736px">Free survival<br>kit included.</div>
    <div class="feature" style="left:106px;top:872px">Eat what you catch</div>
    <div class="feature" style="left:275px;top:876px">Learn essential<br>survival skills</div>
    <div class="feature" style="left:437px;top:871px">Provided buy an<br>experienced and<br>passionate bushman.</div>

    <div class="flyer__text call call--back">CALL US-00 0000 000</div>
    <div class="flyer__text web">www.websitename.com</div>
  </section>

</div>
</body>
</html>
```